Drone company needs a brochure design

We would like a brochure design which compliments our existing logo, website and business card designs.

www.bramblecrest.com.au

```html
<!DOCTYPE html>
<html lang="en">
<head>
<meta charset="utf-8">
<title>Bramble Crest – Drone Brochure</title>
<link href="https://fonts.googleapis.com/css2?family=Montserrat:wght@400;600;700;800&family=Open+Sans:wght@400;600&display=swap" rel="stylesheet">
<style>
  :root{
    --blue:#29a8e0;
    --blue-dark:#1b7fbf;
    --navy:#17334f;
    --ink:#333a40;
    --grey:#6f7880;
    --page:#e7eaee;
    --white:#ffffff;
    --frame:#2f3235;
  }
  *{margin:0;padding:0;box-sizing:border-box;}
  html,body{width:1200px;height:900px;overflow:hidden;background:var(--page);}
  .flyer{position:absolute;left:290px;top:15px;width:620px;height:870px;background:var(--white);overflow:hidden;font-family:"Open Sans",sans-serif;color:var(--ink);box-shadow:0 6px 24px rgba(0,0,0,.18);}
  .flyer-art{position:absolute;inset:0;}
  .brand{position:absolute;left:44px;top:62px;display:flex;align-items:center;gap:10px;}
  .brand-dot{width:16px;height:16px;border-radius:50%;background:var(--navy);}
  .brand-name{font-family:"Montserrat",sans-serif;font-weight:700;font-size:31px;color:var(--navy);letter-spacing:.5px;}
  .section-title{position:absolute;left:40px;display:flex;align-items:center;gap:8px;font-family:"Montserrat",sans-serif;font-weight:800;font-size:17px;color:var(--blue);text-transform:uppercase;letter-spacing:.5px;}
  .section-title::after{content:"";display:block;width:140px;height:1px;background:var(--blue);margin-left:6px;}
  .section-title svg{width:16px;height:16px;fill:var(--navy);}
  .about-title{top:150px;}
  .services-title{top:380px;}
  .body-copy{position:absolute;left:40px;font-size:9.5px;line-height:1.45;color:var(--grey);}
  .about-copy{top:178px;width:280px;}
  .services-copy{top:408px;width:330px;}
  .tagline{position:absolute;left:40px;top:270px;font-family:"Montserrat",sans-serif;font-size:22px;line-height:1.12;color:var(--blue);font-weight:400;}
  .tagline strong{font-weight:700;}
  .service{position:absolute;width:120px;text-align:center;font-family:"Montserrat",sans-serif;font-size:10.5px;font-weight:700;color:var(--navy);line-height:1.15;}
  .service span{color:var(--blue);}
  .service-icon{display:block;width:76px;height:76px;margin:0 auto 6px;}
  .phone-tag{position:absolute;left:400px;top:668px;display:flex;align-items:center;gap:6px;font-family:"Montserrat",sans-serif;font-weight:800;font-size:22px;color:var(--blue);transform:rotate(-4deg);}
  .phone-tag svg{width:22px;height:22px;}
  .web{position:absolute;left:40px;top:822px;font-family:"Montserrat",sans-serif;font-size:19px;letter-spacing:1.5px;color:var(--white);transform:rotate(-5deg);transform-origin:left center;}
</style>
</head>
<body>
<main class="flyer">
  <svg class="flyer-art" viewBox="0 0 620 870" width="620" height="870">
    <defs>
      <linearGradient id="sky" x1="0" y1="0" x2="0" y2="1">
        <stop offset="0" stop-color="#bfe3f5"/>
        <stop offset="1" stop-color="#ffffff"/>
      </linearGradient>
      <linearGradient id="estate" x1="0" y1="0" x2="0" y2="1">
        <stop offset="0" stop-color="#dfe9ef"/>
        <stop offset=".35" stop-color="#8a7a6b"/>
        <stop offset="1" stop-color="#3f7a35"/>
      </linearGradient>
      <linearGradient id="towers" x1="0" y1="0" x2="1" y2="1">
        <stop offset="0" stop-color="#8fb6dc"/>
        <stop offset="1" stop-color="#2c3440"/>
      </linearGradient>
      <linearGradient id="skyline" x1="0" y1="0" x2="0" y2="1">
        <stop offset="0" stop-color="#ffffff" stop-opacity="0"/>
        <stop offset=".35" stop-color="#b5babf"/>
        <stop offset="1" stop-color="#2b2e31"/>
      </linearGradient>
    </defs>
    <rect class="sky-wash" x="0" y="0" width="620" height="250" fill="url(#sky)"/>
    <polygon class="corner-band" points="0,0 150,0 0,52" fill="var(--blue)"/>
    <polygon class="corner-band-shade" points="150,0 175,0 0,62 0,52" fill="var(--blue-dark)"/>

    <rect class="skyline-photo" x="0" y="660" width="620" height="210" fill="url(#skyline)" role="img" aria-label="Black and white aerial photo of a city skyline"/>
    <polygon class="skyline-cut" points="0,790 260,760 260,770 0,804" fill="var(--white)"/>

    <polygon class="photo-frame" points="520,0 620,0 620,418 478,432 350,290" fill="var(--blue)"/>
    <polygon class="estate-photo" points="532,0 620,0 620,404 482,418 366,290" fill="url(#estate)" role="img" aria-label="Aerial drone photo of a house with a tiled roof and green garden, drone hovering above"/>

    <polygon class="towers-frame-shadow" points="530,300 640,410 530,520 420,410" fill="var(--frame)"/>
    <polygon class="towers-frame" points="520,285 628,393 520,501 412,393" fill="var(--blue)"/>
    <polygon class="towers-photo" points="520,296 617,393 520,490 423,393" fill="url(#towers)" role="img" aria-label="Photo of glass skyscrapers against a blue sky"/>

    <polygon class="phone-plate" points="388,676 620,648 620,700 398,726" fill="var(--white)"/>
    <polygon class="phone-plate-edge" points="398,726 620,700 620,706 400,732" fill="var(--blue)"/>
  </svg>

  <div class="brand"><span class="brand-dot"></span><span class="brand-name">Bramble Crest</span></div>

  <h2 class="section-title about-title"><svg viewBox="0 0 16 16"><circle cx="5" cy="5" r="3"/><circle cx="11" cy="5" r="3"/><path d="M0 15c0-4 2-6 5-6s5 2 5 6zM8 15c0-4 1-6 3-6s5 2 5 6z"/></svg>About</h2>
  <p class="body-copy about-copy">We provide premium aerial media solutions using the latest Unmanned Aerial Vehicles (UAV) technology. Offering a combination of stunning HD aerial filming and breathtaking aerial photography for a variety of different projects. The Bramble Crest team offer a unique service that is bespoke to your application and desired specification.</p>

  <p class="tagline"><strong>Let us capture</strong><br>your vision and provide<br>you with that<br><strong>ultimate vantage!</strong></p>

  <h2 class="section-title services-title"><svg viewBox="0 0 16 16"><circle cx="6" cy="9" r="4" fill="none" stroke="#17334f" stroke-width="2.5"/><circle cx="12.5" cy="4" r="2.3" fill="none" stroke="#17334f" stroke-width="1.6"/></svg>Services</h2>
  <p class="body-copy services-copy">We provide premium aerial media solutions using the latest Unmanned Aerial Vehicles (UAV) technology. Offering a combination of stunning HD aerial filming and breathtaking aerial photography for a variety of different projects. The Bramble Crest team offer a unique service that is bespoke to your application and desired specification.</p>

  <div class="service" style="left:40px;top:510px;">
    <svg class="service-icon" viewBox="0 0 76 76"><polygon points="38,6 72,40 38,74 4,40" fill="var(--frame)"/><polygon points="38,2 70,34 38,66 6,34" fill="var(--white)" stroke="var(--blue)" stroke-width="4"/><path d="M26 36 L38 25 L50 36 V46 H26Z" fill="var(--blue)"/></svg>
    Real <span>Estate</span></div>
  <div class="service" style="left:160px;top:495px;">
    <svg class="service-icon" viewBox="0 0 76 76"><polygon points="38,6 72,40 38,74 4,40" fill="var(--frame)"/><polygon points="38,2 70,34 38,66 6,34" fill="var(--white)" stroke="var(--blue)" stroke-width="4"/><path d="M26 46 V28 H34 V46Z M37 46 V22 H50 V46Z" fill="var(--blue)"/></svg>
    Construction <span>&amp;<br>Property</span></div>
  <div class="service" style="left:280px;top:480px;">
    <svg class="service-icon" viewBox="0 0 76 76"><polygon points="38,6 72,40 38,74 4,40" fill="var(--frame)"/><polygon points="38,2 70,34 38,66 6,34" fill="var(--white)" stroke="var(--blue)" stroke-width="4"/><path d="M26 31 H32 L46 23 V45 L32 37 H26Z" fill="var(--blue)"/></svg>
    Media <span>&amp;<br>Advertising</span></div>
  <div class="service" style="left:40px;top:640px;">
    <svg class="service-icon" viewBox="0 0 76 76"><polygon points="38,6 72,40 38,74 4,40" fill="var(--frame)"/><polygon points="38,2 70,34 38,66 6,34" fill="var(--white)" stroke="var(--blue)" stroke-width="4"/><circle cx="36" cy="32" r="8" fill="none" stroke="var(--blue)" stroke-width="4"/><path d="M41 38 L48 45" stroke="var(--blue)" stroke-width="4"/></svg>
    Inspection <span>&amp;<br>Environment</span></div>
  <div class="service" style="left:160px;top:625px;">
    <svg class="service-icon" viewBox="0 0 76 76"><polygon points="38,6 72,40 38,74 4,40" fill="var(--frame)"/><polygon points="38,2 70,34 38,66 6,34" fill="var(--white)" stroke="var(--blue)" stroke-width="4"/><path d="M25 26 L33 23 L42 26 L51 23 V43 L42 46 L33 43 L25 46Z" fill="var(--blue)"/></svg>
    Survey <span>&amp; Mapping</span></div>
  <div class="service" style="left:280px;top:610px;">
    <svg class="service-icon" viewBox="0 0 76 76"><polygon points="38,6 72,40 38,74 4,40" fill="var(--frame)"/><polygon points="38,2 70,34 38,66 6,34" fill="var(--white)" stroke="var(--blue)" stroke-width="4"/><path d="M27 37 a6 6 0 0 1 4-10 a8 8 0 0 1 15 1 a5 5 0 0 1 2 9Z" fill="var(--blue)"/></svg>
    Insurance <span>&amp; Risk</span></div>

  <div class="phone-tag"><svg viewBox="0 0 22 22"><circle cx="11" cy="11" r="9.5" fill="none" stroke="var(--blue)" stroke-width="2"/><path d="M7 6 L9 6 L10 9 L9 10 Q10 12 12 13 L13 12 L16 13 L16 15 Q10 16 7 9Z" fill="var(--blue)"/></svg>040 555 0182</div>

  <p class="web">www.bramblecrest.com.au</p>
</main>
</body>
</html>
```